Rack card for a integrative medical practice

Need an eye-catching rack card with our logo with content as provided. We have a membership based holistic medical practice which incorporates western and holistic medicine. We would like to focus on wellness and healthy lifestyle. See uploaded files for what is included in the membership. Would like 2 page rack card color on both sides. Logo must be on the front.

Target Market(s)

People looking for alternative medicine, healthy lifestyle.

Industry/Entity Type

Health and Wellness

Colors
00AB8E
00BBA5
67D7C9
C6EFE9
E9F9F6

Requirements
Must have
• Must spark interest at first sight. Clear message.
Nice to have
• Warm, bright and positive vibe. Organic, neutral and earthy colors.
Should not have
• Traditional medical practice vibe (cold, formal, industrial). No PINK except the logo.

```html
<!DOCTYPE html>
<html lang="en">
<head>
<meta charset="utf-8">
<title>Meridian Health &amp; Wellness – Rack Card</title>
<link href="https://fonts.googleapis.com/css2?family=Libre+Franklin:wght@300;400;800&display=swap" rel="stylesheet">
<style>
  :root {
    --sun: #f8d24a;
    --sun-top: #f9d85c;
    --sun-glow: #fde99a;
    --rust: #a8512a;
    --gold-line: #c9a050;
    --linen: #f4f1ee;
    --rose: #d7a7b4;
    --sand: #c9a27a;
    --teal-deep: #00ab8e;
    --teal: #00bba5;
    --teal-soft: #67d7c9;
    --teal-mist: #c6efe9;
    --teal-pale: #e9f9f6;
  }
  * { margin: 0; padding: 0; box-sizing: border-box; }
  html, body { width: 1200px; height: 2779px; overflow: hidden; background: #ffffff; }
  .rack-card {
    position: relative;
    width: 1200px;
    height: 2779px;
    overflow: hidden;
    font-family: "Libre Franklin", Arial, sans-serif;
    color: var(--rust);
  }
  .hero-photo {
    position: absolute;
    inset: 0 0 auto 0;
    height: 1300px;
    background:
      radial-gradient(ellipse 520px 700px at 900px 500px, #ffffff 0%, #f7f5f2 55%, transparent 75%),
      radial-gradient(ellipse 420px 300px at 200px 200px, var(--rose) 0%, transparent 70%),
      radial-gradient(ellipse 300px 380px at 360px 620px, var(--sand) 0%, transparent 70%),
      radial-gradient(ellipse 320px 260px at 120px 1050px, #b24a5e 0%, transparent 75%),
      linear-gradient(160deg, #e9dcdc 0%, var(--linen) 45%, #e8d8cf 100%);
  }
  .petal-panel {
    position: absolute;
    left: 0;
    top: 0;
    width: 1200px;
    height: 2779px;
  }
  .ornament {
    position: absolute;
    left: 0;
    top: 1180px;
    width: 330px;
    height: 1500px;
    background: radial-gradient(ellipse 260px 700px at 40px 600px, var(--sun-glow) 0%, rgba(253,233,154,0.4) 50%, transparent 80%);
    opacity: 0.8;
  }
  .brand {
    position: absolute;
    top: 1060px;
    left: 0;
    width: 1200px;
    text-align: center;
    color: var(--rust);
    font-weight: 400;
  }
  .brand-mark {
    display: block;
    width: 170px;
    height: 170px;
    margin: 0 auto 34px;
    border-radius: 50%;
    background: var(--teal);
  }
  .brand-name {
    display: block;
    font-size: 88px;
    line-height: 92px;
    letter-spacing: 0.2em;
    padding-left: 0.2em;
  }
  .brand-tagline {
    display: block;
    margin-top: 8px;
    font-size: 30px;
    line-height: 36px;
    letter-spacing: 0.32em;
    padding-left: 0.32em;
  }
  .headline {
    position: absolute;
    top: 1600px;
    left: 0;
    width: 1200px;
    text-align: center;
    font-weight: 300;
    font-size: 82px;
    line-height: 98px;
    text-transform: uppercase;
    color: var(--rust);
  }
  .headline strong { font-weight: 800; }
  .address {
    position: absolute;
    top: 2505px;
    left: 0;
    width: 1200px;
    text-align: center;
    font-style: normal;
    font-size: 54px;
    line-height: 76px;
    font-weight: 300;
  }
  .address .city { font-weight: 800; }
</style>
</head>
<body>
  <main class="rack-card">
    <div class="hero-photo" role="img" aria-label="Photo of a woman in white linen sitting cross-legged on patterned cushions, hand resting on her chest"></div>

    <svg class="petal-panel" viewBox="0 0 1200 2779" aria-hidden="true">
      <defs>
        <linearGradient id="sunFill" x1="0" y1="0" x2="0" y2="1">
          <stop offset="0" stop-color="#f9d85c"/>
          <stop offset="1" stop-color="#f7cf42"/>
        </linearGradient>
      </defs>
      <path d="M0 1178 Q120 1150 245 1152 C 238 1060 226 950 218 866 C 330 892 420 940 469 1003 C 515 905 560 815 598 768 C 638 815 682 905 730 997 C 782 940 875 892 986 866 C 976 950 966 1060 959 1155 Q1080 1160 1200 1190 L1200 2779 L0 2779 Z" fill="url(#sunFill)"/>
      <path d="M0 1178 Q120 1150 245 1152 C 238 1060 226 950 218 866 C 330 892 420 940 469 1003 C 515 905 560 815 598 768 C 638 815 682 905 730 997 C 782 940 875 892 986 866 C 976 950 966 1060 959 1155 Q1080 1160 1200 1190" fill="none" stroke="var(--gold-line)" stroke-width="8" opacity="0.8"/>
    </svg>

    <div class="ornament" role="img" aria-label="Faint paisley mandala ornament along the left edge"></div>

    <h1 class="brand">
      <span class="brand-mark" aria-hidden="true"></span>
      <span class="brand-name">MERIDIAN</span>
      <span class="brand-tagline">HEALTH &amp; WELLNESS</span>
    </h1>

    <p class="headline">
      A <strong>Direct Primary</strong><br>
      Care Practice<br>
      Focused on a More<br>
      <strong>Holistic</strong> and<br>
      <strong>Personal</strong><br>
      <strong>Approach</strong> to<br>
      Medicine.
    </p>

    <address class="address">
      1247 Elm Grove Ave., STE 2B<br>
      <span class="city">Riverton</span>
    </address>
  </main>
</body>
</html>
```